Ashford Church of Grace (this will be used for new church sign) sign will be 4'x8' and would like also listed Sunday School 9:00am Worship Service 10:30am.

Logo Text

ASHFORD CHURCH OF GRACE

```html
<!DOCTYPE html>
<html lang="en">
<head>
<meta charset="utf-8">
<title>Ashford Church of Grace – Sign</title>
<link rel="stylesheet" href="https://fonts.googleapis.com/css2?family=Bebas+Neue&display=swap">
<style>
  :root {
    --page-bg: #d9d9d9;
    --sign-white: #ffffff;
    --brand-cyan: #06a6d4;
    --brand-navy: #07598c;
    --shadow: rgba(0, 0, 0, 0.35);
  }
  html, body {
    margin: 0;
    padding: 0;
    width: 1061px;
    height: 1200px;
    overflow: hidden;
    background: var(--page-bg);
  }
  .canvas {
    position: relative;
    width: 1061px;
    height: 1200px;
  }
  .church-sign {
    position: absolute;
    left: 80px;
    top: 375px;
    width: 900px;
    height: 450px;
    filter: drop-shadow(2px 4px 3px var(--shadow));
  }
  .church-sign svg { display: block; }
  .sign-text { font-family: 'Bebas Neue', 'Oswald', sans-serif; }
  .name-top { fill: var(--brand-cyan); font-size: 216px; }
  .name-bottom { fill: var(--brand-navy); font-size: 166px; }
  .service-times { fill: var(--sign-white); font-size: 44px; }
  .sign-face { fill: var(--sign-white); stroke: var(--brand-cyan); stroke-width: 9; }
  .service-band { fill: var(--brand-cyan); }
</style>
</head>
<body>
<main class="canvas">
  <div class="church-sign">
    <svg width="900" height="450" viewBox="0 0 900 450" role="group" aria-label="Ashford Church of Grace sign">
      <rect class="sign-face" x="4.5" y="4.5" width="891" height="441"/>
      <text class="sign-text name-top" x="49" y="194" textLength="807" lengthAdjust="spacing">ASHFORD</text>
      <text class="sign-text name-bottom" x="41" y="330" textLength="818" lengthAdjust="spacingAndGlyphs">CHURCH OF GRACE</text>
      <rect class="service-band" x="40" y="347" width="820" height="58"/>
      <text class="sign-text service-times" x="55" y="392" textLength="789" lengthAdjust="spacing">SUNDAY SCHOOL 9:00AM WORSHIP SERVICE 10:30AM.</text>
    </svg>
  </div>
</main>
</body>
</html>
```